Business Card for Freelance Copywriting & Web Design Business

Hi! I have a logo but want a new business card. Here's a better idea of what I'm thinking:
-Brand new double-sided business card, rounded cards, embossed logo, nice quality paper
-Include phone (604-382-5194), email (hello@lauraberndt.org), and website (www.lauraberndt.org). No address, please, since I service clients worldwide.
-I'd like the fonts to match those on my website (www.lauraberndt.org). I had to purchase the one font (Born Ready), attached. I'm not sure which version was used on my site so I included all that I purchased. The secondary font is Helvetica
-I'd also like the tagline "Powerful Words. Impressive Results." included.
-My primary brand colour is the teal, colour #19ADC3
Laura Berndt | Laura Berndt Copywriting & Web Design <hello@lauraberndt.org>
-I'd also like the following services listed on the new cards:
SEO Website Content
SEO Blog Content
SEO Website Design
Contact Information for Business Card
as stated in brief
Font styles to use
Other font styles liked:
- See brief
Look and feel
Each slider illustrates characteristics of the customer's brand and the style your logo design should communicate.

```html
<!DOCTYPE html>
<html lang="en">
<head>
<meta charset="utf-8">
<title>Laura Berndt – Business Card</title>
<link rel="stylesheet" href="https://fonts.googleapis.com/css2?family=Arimo:wght@400;700&display=swap">
<style>
  :root {
    --page-bg: #d3d6d7;
    --brand-teal: #12aec6;
    --soft-teal: #7fb8c4;
    --frame-teal: #7bb7c3;
    --light-teal: #93c6d1;
    --ink: #111111;
    --paper: #ffffff;
  }
  * { box-sizing: border-box; margin: 0; padding: 0; }
  html, body {
    width: 1200px; height: 960px; overflow: hidden;
    background: var(--page-bg);
    font-family: "Arimo", "Helvetica Neue", Helvetica, Arial, sans-serif;
  }
  .card {
    position: absolute; left: 249px; width: 702px; height: 400px;
    border-radius: 22px; overflow: hidden;
  }
  .card--front { top: 60px; background: var(--brand-teal); }
  .card--back { top: 501px; background: var(--paper); border: 4px solid var(--frame-teal); }

  .wordmark { position: absolute; color: var(--ink); font-weight: 400; white-space: nowrap; }
  .card--front .wordmark { left: 0; right: 0; top: 148px; text-align: center; font-size: 64px; letter-spacing: 1px; }
  .card--back .wordmark { left: 32px; top: 92px; font-size: 46px; letter-spacing: 1px; }

  .services { position: absolute; left: 0; right: 0; top: 327px; text-align: center; color: var(--paper); }
  .services__title { font-size: 20px; letter-spacing: 0.5px; }
  .services__list { list-style: none; display: flex; justify-content: center; gap: 12px; margin-top: 6px; font-size: 17px; }
  .services__list li::before { content: "\25CF"; margin-right: 8px; font-size: 13px; position: relative; top: -2px; }

  .tagline { position: absolute; left: 20px; top: 237px; color: var(--soft-teal); font-size: 16px; line-height: 22px; }
  .contact { position: absolute; left: 20px; top: 300px; list-style: none; font-size: 16px; color: var(--ink); }
  .contact li { display: flex; align-items: center; gap: 8px; height: 23.5px; }
  .contact svg { width: 16px; height: 16px; }

  .identity { position: absolute; right: 35px; top: 164px; text-align: right; }
  .identity__name { color: var(--light-teal); font-size: 33px; font-weight: 700; letter-spacing: 0.5px; }
  .identity__role { color: var(--ink); font-size: 17px; margin-top: 4px; }
  .identity__bar { position: absolute; right: 0; top: 166px; width: 16px; height: 62px; background: var(--frame-teal); }
</style>
</head>
<body>
  <section class="card card--front" aria-label="Card front">
    <div class="wordmark">Laura Berndt</div>
    <div class="services">
      <h2 class="services__title" style="font-weight:400">SERVICES</h2>
      <ul class="services__list">
        <li>SEO Website Content</li>
        <li>SEO Blog Content</li>
        <li>SEO Website Design</li>
      </ul>
    </div>
  </section>

  <section class="card card--back" aria-label="Card back">
    <div class="wordmark">Laura Berndt</div>

    <p class="tagline">Powerful Words.<br>Impressive Results.</p>

    <ul class="contact">
      <li>
        <svg viewBox="0 0 16 16" aria-hidden="true"><path d="M3.5 1.5l2.5 3-1.5 1.5c.8 2 2.5 3.7 4.5 4.5l1.5-1.5 3 2.5-1.8 2.3C7 13.5 2.5 9 1.2 3.3z" fill="none" stroke="var(--soft-teal)" stroke-width="1.4" stroke-linejoin="round"/></svg>
        <span>(604-382-5194)</span>
      </li>
      <li>
        <svg viewBox="0 0 16 16" aria-hidden="true"><circle cx="8" cy="8" r="6.6" fill="none" stroke="var(--soft-teal)" stroke-width="1.4"/><path d="M1.5 8h13M8 1.5c-3 3.5-3 9.5 0 13M8 1.5c3 3.5 3 9.5 0 13" fill="none" stroke="var(--soft-teal)" stroke-width="1.1"/></svg>
        <span>www.lauraberndt.org</span>
      </li>
      <li>
        <svg viewBox="0 0 16 16" aria-hidden="true"><rect x="1.2" y="4" width="13.6" height="10" rx="1" fill="none" stroke="var(--soft-teal)" stroke-width="1.4"/><path d="M1.5 4.5L8 9.5l6.5-5" fill="none" stroke="var(--soft-teal)" stroke-width="1.4"/></svg>
        <span>hello@lauraberndt.org</span>
      </li>
    </ul>

    <div class="identity">
      <div class="identity__name">Laura Berndt</div>
      <div class="identity__role">Copywriting &amp; Web Design</div>
    </div>
    <div class="identity__bar"></div>
  </section>
</body>
</html>
```